Business card for my company-RKV Design Studio

I do not have a logo-I like red and keeping it clean. Information that should be on the card:
Tom Brazenhall AIA
Architecture Planning Interiors
Cell Phone-614.529.4086
email-rkvplanner4@mailvane.net
www.rkvdesignstudio.net

```html
<!DOCTYPE html>
<html lang="en">
<head>
<meta charset="utf-8">
<title>RKV Design Studio – Business Card</title>
<link href="https://fonts.googleapis.com/css2?family=Montserrat:wght@500;800&family=Arimo:wght@400&display=swap" rel="stylesheet">
<style>
  :root {
    --red: #e60000;
    --red-light: #f03a3a;
    --white: #ffffff;
    --ink: #333333;
    --stage: #343434;
  }
  * { margin: 0; padding: 0; box-sizing: border-box; }
  html, body { width: 1200px; height: 866px; overflow: hidden; }
  body {
    background: var(--stage);
    display: flex;
    align-items: center;
    justify-content: center;
    gap: 40px;
  }
  .card {
    position: relative;
    width: 540px;
    height: 309px;
    overflow: hidden;
  }

  /* Front */
  .card-front { background: var(--white); }
  .card-front .band {
    position: absolute; left: 0; bottom: 0; width: 540px; height: 80px;
  }
  .holder {
    position: absolute; left: 30px; top: 44px;
    font-family: "Montserrat", sans-serif;
  }
  .holder-name {
    color: var(--red); font-weight: 800; font-size: 19px; letter-spacing: 0.5px;
    text-transform: uppercase;
  }
  .holder-role {
    font-family: "Arimo", sans-serif; color: var(--ink); font-size: 14px; margin-top: 1px;
  }
  .holder-rule {
    position: absolute; left: 30px; top: 98px; width: 470px; height: 1px;
    background: var(--red); transform-origin: left; transform: rotate(14deg);
  }
  .contact {
    position: absolute; left: 30px; top: 112px; list-style: none;
    font-family: "Arimo", sans-serif; color: var(--ink); font-size: 14px;
  }
  .contact li { display: flex; align-items: center; gap: 8px; height: 22px; }
  .contact svg { width: 14px; height: 14px; flex: none; }
  .studio-name {
    position: absolute; right: 34px; top: 118px; text-align: right;
    font-family: "Montserrat", sans-serif; font-weight: 800; color: var(--red);
    font-size: 32px; line-height: 1.05; text-transform: uppercase;
  }
  .website {
    position: absolute; right: 30px; bottom: 14px;
    font-family: "Arimo", sans-serif; color: var(--white); font-size: 14px; letter-spacing: 0.5px;
  }

  /* Back */
  .card-back {
    background: var(--red);
    display: flex; align-items: center; justify-content: center;
  }
  .card-back .studio-name {
    position: static; color: var(--white); text-align: center; font-size: 42px;
  }
</style>
</head>
<body>

  <section class="card card-front" aria-label="Card front">
    <svg class="band" viewBox="0 0 540 80" preserveAspectRatio="none" aria-hidden="true">
      <path d="M0 44 H200 C220 44 222 36 240 36 H540 V80 H0 Z" fill="var(--red)"/>
      <path d="M0 34 H196 C212 34 214 30 222 28" fill="none" stroke="var(--red)" stroke-width="2"/>
      <rect x="0" y="48" width="200" height="2" fill="var(--white)"/>
    </svg>

    <div class="holder">
      <p class="holder-name">Tom Brazenhall AIA</p>
      <p class="holder-role">Architecture Planning Interiors</p>
    </div>

    <ul class="contact">
      <li>
        <svg viewBox="0 0 14 14" aria-hidden="true"><rect x="3" y="1" width="8" height="12" rx="1.5" fill="none" stroke="var(--red)" stroke-width="1.5"/><circle cx="7" cy="11" r="0.8" fill="var(--red)"/></svg>
        614.529.4086
      </li>
      <li>
        <svg viewBox="0 0 14 14" aria-hidden="true"><rect x="1" y="3" width="12" height="8" fill="var(--red)"/><path d="M1 3 L7 8 L13 3" fill="none" stroke="var(--white)" stroke-width="1"/></svg>
        rkvplanner4@mailvane.net
      </li>
    </ul>

    <p class="studio-name">RKV<br>Design Studio</p>

    <p class="website">www.rkvdesignstudio.net</p>
  </section>

  <section class="card card-back" aria-label="Card back">
    <p class="studio-name">RKV<br>Design Studio</p>
  </section>

</body>
</html>
```